Powerpoint template for our Credentials presentation for our new consulting business - Channel Spen

We are a new company called Channel Spend Clearview (CSC) based in Sydney Australia

We have both run media buying agencies for many years.

Those agencies run by multi-national organisations are becoming less and less transparent with the transactions that they are managing – clients are being significantly over-charged in many areas – especially digital media.

At the same time, our experience has told us that most clients have little understanding of how media should be planned and bought

We are making ourselves available to those clients who cant afford a full time specialist but want to ensure that they are making the correct media and marketing decisions that benefit them rather than their agency.

Target Market(s)

Marketing Managers and Directors

Industry/Entity Type

Media

Other font styles liked:
• Font used in our logo (attached)

Colors
33a6d7
fbee3e
ffffff

Requirements
Must have
• We have provided the logo that represents the look and feel of the company.
• Please incorporate these colours - blue, yellow and white - into the powerpoint template

```html
<!DOCTYPE html>
<html lang="en">
<head>
<meta charset="utf-8">
<title>Channel Spend Clearview – Credentials Template</title>
<link href="https://fonts.googleapis.com/css2?family=Lato:wght@300;400;700;900&display=swap" rel="stylesheet">
<style>
  :root {
    --blue: #3d7bc6;
    --blue-deep: #2f63a8;
    --yellow: #d6d42c;
    --white: #ffffff;
    --ink: #2b2b2b;
    --grey: #9a9a9a;
    --line: #c9d6e8;
    --canvas: #111111;
  }
  * { margin: 0; padding: 0; box-sizing: border-box; }
  html, body { width: 1200px; height: 1200px; overflow: hidden; background: var(--canvas); }
  body { position: relative; font-family: "Lato", sans-serif; color: var(--ink); }

  .slide { position: absolute; width: 370px; height: 208px; background: var(--white); overflow: hidden; }
  .c1 { left: 21px; } .c2 { left: 416px; } .c3 { left: 805px; }
  .r1 { top: 16px; } .r2 { top: 248px; } .r3 { top: 477px; } .r4 { top: 707px; } .r5 { top: 941px; }

  .abs { position: absolute; }
  .brand { position: absolute; left: 10px; top: 9px; display: flex; gap: 3px; align-items: flex-start; }
  .brand-mark { width: 18px; height: 18px; background: var(--blue); }
  .brand-name { width: 34px; font-size: 4.4px; line-height: 5.2px; font-weight: 700; color: var(--blue); }
  .pager { position: absolute; right: 32px; top: 12px; width: 10px; height: 10px; border-radius: 50%; background: var(--blue); }
  .subtitle { position: absolute; left: 0; right: 0; top: 13px; text-align: center; font-size: 5.2px; color: var(--grey); }
  .title { position: absolute; left: 0; right: 0; top: 21px; text-align: center; font-size: 11.5px; font-weight: 400; color: var(--ink); }
  .rule { position: absolute; left: 178px; top: 40px; width: 14px; height: 1.3px; background: var(--yellow); }
  .footer { position: absolute; left: 26px; bottom: 8px; font-size: 3.6px; color: #b5b5b5; }
  .footer b { color: #8f8f8f; }

  .body-text { font-size: 3.7px; line-height: 5.6px; color: #9a9a9a; text-align: justify; }
  .body-text p + p { margin-top: 6px; }

  .photo { position: absolute; }
  .photo-desk { background: linear-gradient(135deg, #8a6a4a, #b48a5e 45%, #6e5238); }
  .photo-desk-blue { background: linear-gradient(135deg, #3c6fb4, #5d8bcc 50%, #2d5a9a); }
  .photo-portrait { background: linear-gradient(160deg, #e9e9e9, #cfcfcf); }
  .photo-meeting { background: linear-gradient(120deg, #2a2d33, #8d8f94 45%, #d8d8da 70%, #4a4c52); }

  .track { position: absolute; height: 1.2px; background: var(--blue); top: 103px; }
  .node { position: absolute; top: 93px; width: 20px; height: 20px; margin-left: -10px; border-radius: 50%;
          background: var(--blue); border: 2px solid #bcd0ea; color: var(--white); font-size: 3.6px; line-height: 4px;
          display: flex; align-items: center; justify-content: center; text-align: center; }
  .node.alt { background: var(--yellow); border-color: #efeeb6; }
  .node-label { position: absolute; top: 122px; width: 80px; margin-left: -40px; text-align: center; font-size: 5px; font-weight: 700; color: var(--ink); }
  .node-cap { position: absolute; top: 130px; width: 60px; margin-left: -30px; text-align: center; font-size: 3.6px; line-height: 5px; color: #b0b0b0; }

  .vline { position: absolute; width: 1.2px; background: var(--blue); }
  .dot { position: absolute; width: 5px; height: 5px; margin: -2.5px 0 0 -2.4px; border-radius: 50%; background: var(--blue); }
  .mile { position: absolute; font-size: 7.5px; font-weight: 700; line-height: 8px; }
  .mile small { display: block; font-size: 3.8px; font-weight: 400; color: #b0b0b0; margin-top: 2px; }
  .mile.l { text-align: right; }
  .mile.blue { color: var(--blue); } .mile.gold { color: var(--yellow); } .mile.dark { color: var(--ink); }

  .sol { position: absolute; width: 80px; margin-left: -40px; text-align: center; }
  .sol svg { width: 18px; height: 18px; stroke: var(--blue); fill: none; stroke-width: 1.4; }
  .sol h4 { font-size: 5px; font-weight: 700; color: var(--ink); margin-top: 3px; }
  .sol p { font-size: 3.6px; line-height: 5px; color: #b5b5b5; }
</style>
</head>
<body>

<!-- Cover -->
<section class="slide c1 r1">
  <div class="photo photo-desk-blue" style="inset:0" role="img" aria-label="Team working around a desk with laptops and charts, blue tint"></div>
  <div class="abs" style="left:0;right:0;top:30px;display:flex;justify-content:center;align-items:center;gap:4px;">
    <div style="width:12px;height:12px;background:var(--yellow)"></div>
    <div style="font-size:6px;font-weight:700;color:var(--white)">Channel Spend Clearview</div>
  </div>
  <div class="abs" style="left:0;right:0;top:70px;text-align:center;color:var(--white);font-weight:900;font-size:24px;line-height:26px;letter-spacing:0.5px;">BUSINESS<br>PROPOSAL</div>
  <div class="abs" style="left:0;right:0;top:128px;text-align:center;color:#d6e3f4;font-size:5px;">Creative Presentation Template</div>
  <div class="abs" style="left:0;right:0;top:184px;text-align:center;color:#d6e3f4;font-size:3.6px;">Presented by CSC</div>
</section>

<!-- Text in one column -->
<section class="slide c2 r1">
  <div class="brand"><div class="brand-mark"></div><div class="brand-name">Channel Spend Clearview</div></div>
  <div class="pager"></div>
  <div class="subtitle">Insert your subtitle text here</div>
  <div class="title">Text in One Column</div>
  <div class="rule"></div>
  <div class="abs body-text" style="left:34px;right:34px;top:58px;">
    <p>Independent media advice helps marketers see where every dollar goes, which fees apply, and how plans compare with real market rates across digital and traditional channels.</p>
    <p>Independent media advice helps marketers see where every dollar goes, which fees apply, and how plans compare with real market rates across digital and traditional channels.</p>
  </div>
  <div class="footer"><b>Business</b> Presentation</div>
</section>

<!-- Text in two columns -->
<section class="slide c3 r1">
  <div class="brand"><div class="brand-mark"></div><div class="brand-name">Channel Spend Clearview</div></div>
  <div class="pager"></div>
  <div class="subtitle">Insert your subtitle text here</div>
  <div class="title">Text In Two Columns</div>
  <div class="rule"></div>
  <div class="abs body-text" style="left:36px;width:138px;top:54px;">
    <p>Independent media advice helps marketers see where every dollar goes, which fees apply, and how plans compare with real market rates across digital and traditional channels.</p>
    <p>Independent media advice helps marketers see where every dollar goes, which fees apply, and how plans compare with real market rates across digital and traditional channels.</p>
  </div>
  <div class="abs body-text" style="left:194px;width:138px;top:54px;">
    <p>Independent media advice helps marketers see where every dollar goes, which fees apply, and how plans compare with real market rates across digital and traditional channels.</p>
    <p>Independent media advice helps marketers see where every dollar goes, which fees apply, and how plans compare with real market rates across digital and traditional channels.</p>
  </div>
  <div class="footer"><b>Business</b> Presentation</div>
</section>

<!-- Text in three columns -->
<section class="slide c1 r2">
  <div class="brand"><div class="brand-mark"></div><div class="brand-name">Channel Spend Clearview</div></div>
  <div class="pager"></div>
  <div class="subtitle">Insert your subtitle text here</div>
  <div class="title">Text In Three Columns</div>
  <div class="rule"></div>
  <div class="abs body-text" style="left:36px;width:92px;top:52px;">
    <p>Independent media advice helps marketers see where every dollar goes, which fees apply, and how plans compare with real market rates across digital and traditional channels.</p>
    <p>Independent media advice helps marketers see where every dollar goes, which fees apply, and how plans compare with real market rates across digital and traditional channels.</p>
  </div>
  <div class="abs body-text" style="left:139px;width:92px;top:52px;">
    <p>Independent media advice helps marketers see where every dollar goes, which fees apply, and how plans compare with real market rates across digital and traditional channels.</p>
    <p>Independent media advice helps marketers see where every dollar goes, which fees apply, and how plans compare with real market rates across digital and traditional channels.</p>
  </div>
  <div class="abs body-text" style="left:242px;width:92px;top:52px;">
    <p>Independent media advice helps marketers see where every dollar goes, which fees apply, and how plans compare with real market rates across digital and traditional channels.</p>
    <p>Independent media advice helps marketers see where every dollar goes, which fees apply, and how plans compare with real market rates across digital and traditional channels.</p>
  </div>
  <div class="footer"><b>Business</b> Presentation</div>
</section>

<!-- Content overview 1 -->
<section class="slide c2 r2">
  <div class="brand"><div class="brand-mark"></div><div class="brand-name">Channel Spend Clearview</div></div>
  <div class="pager"></div>
  <div class="subtitle">Insert your subtitle text here</div>
  <div class="title">Presentation Content Overview</div>
  <div class="rule"></div>
  <div class="track" style="left:73px;right:0;"></div>
  <div class="abs" style="left:28px;top:80px;width:46px;height:46px;border-radius:50%;border:1px solid #d5e1f0;background:var(--white);display:flex;align-items:center;justify-content:center;">
    <svg width="18" height="18" viewBox="0 0 24 24" fill="none" stroke="#3d7bc6" stroke-width="1.6"><path d="M3 11 12 3l9 8"/><path d="M5 10v11h14V10"/><path d="M10 21v-6h4v6"/></svg>
  </div>
  <div class="node" style="left:153px;">9:00<br>AM</div>
  <div class="node-label" style="left:153px;">WELCOME MESSAGE</div>
  <div class="node-cap" style="left:153px;">Tools that allow people or companies to create, share</div>
  <div class="node" style="left:260px;">9:15<br>AM</div>
  <div class="node-label" style="left:260px;">ABOUT US</div>
  <div class="node-cap" style="left:260px;">Tools that allow people or companies to create, share</div>
  <div class="footer"><b>Business</b> Presentation</div>
</section>

<!-- Content overview 2 -->
<section class="slide c3 r2">
  <div class="brand"><div class="brand-mark"></div><div class="brand-name">Channel Spend Clearview</div></div>
  <div class="pager"></div>
  <div class="track" style="left:0;right:0;"></div>
  <div class="node" style="left:58px;">9:30<br>AM</div>
  <div class="node-label" style="left:58px;">OUR SERVICES</div>
  <div class="node-cap" style="left:58px;">Tools that allow people or companies to create, share</div>
  <div class="node alt" style="left:180px;">10:00<br>AM</div>
  <div class="node-label" style="left:180px;">OUR SOLUTIONS</div>
  <div class="node-cap" style="left:180px;">Tools that allow people or companies to create, share</div>
  <div class="node" style="left:309px;">11:00<br>AM</div>
  <div class="node-label" style="left:309px;">THE PROBLEM</div>
  <div class="node-cap" style="left:309px;">Tools that allow people or companies to create, share</div>
  <div class="footer"><b>Business</b> Presentation</div>
</section>

<!-- Content overview 3 -->
<section class="slide c1 r3">
  <div class="brand"><div class="brand-mark"></div><div class="brand-name">Channel Spend Clearview</div></div>
  <div class="pager"></div>
  <div class="track" style="left:0;width:260px;"></div>
  <div class="node" style="left:57px;">12:30<br>PM</div>
  <div class="node-label" style="left:57px;">MEET THE TEAM</div>
  <div class="node-cap" style="left:57px;">Tools that allow people or companies to create, share</div>
  <div class="node alt" style="left:179px;">01:00<br>PM</div>
  <div class="node-label" style="left:179px;">OUR WORKS</div>
  <div class="node-cap" style="left:179px;">Tools that allow people or companies to create, share</div>
  <div class="abs" style="left:259px;top:81px;width:46px;height:46px;border-radius:50%;border:1px solid #d5e1f0;display:flex;align-items:center;justify-content:center;font-size:6px;font-weight:700;">FINISH</div>
  <div class="footer"><b>Business</b> Presentation</div>
</section>

<!-- Our team / business -->
<section class="slide c2 r3">
  <div class="photo photo-portrait" style="left:0;top:0;width:185px;height:104px;" role="img" aria-label="Portrait photo of a team member"></div>
  <div class="pager"></div>
  <div class="abs" style="left:198px;top:18px;width:140px;">
    <div style="font-size:5.6px;font-weight:700;">Our Team</div>
    <div style="font-size:3.6px;color:var(--yellow);margin:1px 0 5px;">Your Text Here</div>
    <div class="body-text" style="text-align:left;"><p>Our partners have run media agencies for years and now offer clear, honest guidance to clients.</p><p>Our partners have run media agencies for years and now offer clear, honest guidance to clients.</p></div>
  </div>
  <div class="abs" style="left:38px;top:116px;width:138px;text-align:right;">
    <div style="font-size:5.6px;font-weight:700;">Our Business</div>
    <div style="font-size:3.6px;color:var(--yellow);margin:1px 0 5px;">Your Text Here</div>
    <div class="body-text" style="text-align:right;"><p>Our partners have run media agencies for years and now offer clear, honest guidance to clients.</p><p>Our partners have run media agencies for years and now offer clear, honest guidance to clients.</p></div>
  </div>
  <div class="photo photo-desk" style="left:185px;top:104px;width:185px;height:104px;" role="img" aria-label="Overhead view of a meeting table with laptops, papers and a plant"></div>
  <div class="footer"><b>Business</b> Presentation</div>
</section>

<!-- History 1 -->
<section class="slide c3 r3">
  <div class="brand"><div class="brand-mark"></div><div class="brand-name">Channel Spend Clearview</div></div>
  <div class="pager"></div>
  <div class="subtitle">Insert your subtitle text here</div>
  <div class="title">Our History Through The Time</div>
  <div class="vline" style="left:187px;top:54px;height:154px;"></div>
  <div class="dot" style="left:187px;top:56px;"></div>
  <div class="dot" style="left:187px;top:83px;"></div>
  <div class="dot" style="left:187px;top:114px;"></div>
  <div class="dot" style="left:187px;top:150px;"></div>
  <div class="dot" style="left:187px;top:178px;"></div>
  <div class="mile l blue" style="right:206px;top:52px;">FUNDATION<small>1980</small></div>
  <div class="mile blue" style="left:206px;top:78px;">OPENED NEW<br>LOCATIONS<small>1986</small></div>
  <div class="mile l gold" style="right:206px;top:110px;">BIG CONTRACT<small>2000</small></div>
  <div class="mile blue" style="left:206px;top:146px;">NEW MEMBERS<small>2006</small></div>
  <div class="mile l gold" style="right:206px;top:174px;">COUNTRIES<small>2010</small></div>
  <div class="footer"><b>Business</b> Presentation</div>
</section>

<!-- History 2 -->
<section class="slide c1 r4">
  <div class="brand"><div class="brand-mark"></div><div class="brand-name">Channel Spend Clearview</div></div>
  <div class="pager"></div>
  <div class="vline" style="left:187px;top:0;height:146px;"></div>
  <div class="dot" style="left:187px;top:17px;"></div>
  <div class="dot" style="left:187px;top:43px;"></div>
  <div class="dot" style="left:187px;top:75px;"></div>
  <div class="dot" style="left:187px;top:111px;"></div>
  <div class="dot" style="left:187px;top:138px;"></div>
  <div class="mile l blue" style="right:206px;top:13px;">NEW LOCATIONS<small>2011</small></div>
  <div class="mile blue" style="left:206px;top:40px;">1,000,000<br>MEMBERS<small>2013</small></div>
  <div class="mile l dark" style="right:206px;top:72px;">100K SALES<small>2015</small></div>
  <div class="mile blue" style="left:206px;top:108px;">NEW STORE<small>2019</small></div>
  <div class="mile l gold" style="right:206px;top:135px;">LIVE NOW<small>2020</small></div>
  <div class="footer"><b>Business</b> Presentation</div>
</section>

<!-- Company profile -->
<section class="slide c2 r4">
  <div class="photo photo-desk" style="inset:0" role="img" aria-label="Overhead view of a meeting table with tablet, charts and a plant"></div>
  <div class="abs" style="left:188px;top:-15px;width:240px;height:240px;border-radius:50%;background:var(--blue);opacity:0.95;"></div>
  <div class="abs" style="left:253px;top:52px;width:92px;height:1px;background:var(--yellow);"></div>
  <div class="abs" style="right:26px;top:70px;text-align:right;color:var(--white);font-weight:900;font-size:21px;line-height:25px;letter-spacing:0.5px;">COMPANY<br>PROFILE</div>
  <div class="abs" style="right:26px;top:126px;color:#cfe0f4;font-size:5px;">Your great headline text here</div>
  <div class="abs" style="left:253px;top:152px;width:92px;height:1px;background:var(--yellow);"></div>
</section>

<!-- CEO message -->
<section class="slide c3 r4">
  <div class="brand"><div class="brand-mark"></div><div class="brand-name">Channel Spend Clearview</div></div>
  <div class="pager"></div>
  <div class="subtitle">Insert your subtitle text here</div>
  <div class="title">Message From Our CEO</div>
  <div class="rule"></div>
  <div class="abs" style="left:0;top:62px;width:100%;height:108px;background:var(--blue);"></div>
  <div class="abs" style="left:38px;top:94px;width:150px;color:var(--white);">
    <div style="font-size:6px;font-weight:700;margin-bottom:5px;">HAPPY CUSTOMERS</div>
    <div style="font-size:5px;line-height:7px;">“Mobile social media refers to the combination of mobile devices and social media. This is a group of mobile marketing applications”</div>
  </div>
  <div class="abs" style="right:32px;top:92px;text-align:right;color:var(--white);font-weight:900;font-size:16px;line-height:20px;">Our<br>Top Priority</div>
  <div class="footer"><b>Business</b> Presentation</div>
</section>

<!-- Mission -->
<section class="slide c1 r5">
  <div class="photo photo-meeting" style="inset:0" role="img" aria-label="Business people seated on chairs in a waiting area"></div>
  <div class="abs" style="left:240px;top:0;width:130px;height:100%;background:var(--blue);opacity:0.92;"></div>
  <div class="abs" style="right:27px;top:40px;width:110px;text-align:right;color:var(--white);">
    <div style="font-size:16px;font-weight:900;line-height:19px;">Our<br>Mission</div>
    <div style="font-size:6.4px;line-height:9.4px;margin-top:12px;">Mobile social media refers to the combination of mobile devices and social media. This is a group of mobile marketing applications that allow the creation and exchange of user.</div>
    <div style="font-size:5.6px;font-weight:700;margin-top:8px;">Daniel Hart</div>
  </div>
</section>

<!-- Vision -->
<section class="slide c2 r5">
  <div class="photo photo-meeting" style="inset:0" role="img" aria-label="Business people seated on chairs in a waiting area"></div>
  <div class="abs" style="left:0;top:0;width:138px;height:100%;background:var(--blue);opacity:0.92;"></div>
  <div class="abs" style="left:27px;top:40px;width:110px;color:var(--white);">
    <div style="font-size:16px;font-weight:900;line-height:19px;">Our<br>Vision</div>
    <div style="font-size:6.4px;line-height:9.4px;margin-top:12px;">Mobile social media refers to the combination of mobile devices and social media. This is a group of mobile marketing applications that allow the creation and exchange of user.</div>
    <div style="font-size:5.6px;font-weight:700;margin-top:8px;">Daniel Hart</div>
  </div>
</section>

<!-- Solutions -->
<section class="slide c3 r5">
  <div class="brand"><div class="brand-mark"></div><div class="brand-name">Channel Spend Clearview</div></div>
  <div class="pager"></div>
  <div class="subtitle">Insert your subtitle text here</div>
  <div class="title">Our Solutions</div>
  <div class="rule"></div>
  <div class="sol" style="left:71px;top:60px;"><svg viewBox="0 0 24 24"><path d="M3 11 12 3l9 8M5 10v11h14V10M10 21v-6h4v6"/></svg><h4>Welcome</h4><p>Tools that allow people companies to create content</p></div>
  <div class="sol" style="left:154px;top:60px;"><svg viewBox="0 0 24 24"><path d="M3 10v4h4l9 5V5L7 10H3zM7 14l2 6h3l-2-6M19 9v6"/></svg><h4>Advertising</h4><p>Tools that allow people companies to create content</p></div>
  <div class="sol" style="left:235px;top:60px;"><svg viewBox="0 0 24 24"><circle cx="12" cy="12" r="9"/><circle cx="12" cy="12" r="4"/><path d="M5.6 5.6l3.6 3.6M18.4 5.6l-3.6 3.6M5.6 18.4l3.6-3.6M18.4 18.4l-3.6-3.6"/></svg><h4>Support</h4><p>Tools that allow people companies to create content</p></div>
  <div class="sol" style="left:317px;top:60px;"><svg viewBox="0 0 24 24"><path d="M12 3 2 8l10 5 10-5-10-5zM2 12l10 5 10-5M2 16l10 5 10-5"/></svg><h4>Layers</h4><p>Tools that allow people companies to create content</p></div>
  <div class="sol" style="left:71px;top:127px;"><svg viewBox="0 0 24 24"><rect x="4" y="5" width="16" height="11"/><path d="M2 19h20"/></svg><h4>Devices</h4><p>Tools that allow people companies to create content</p></div>
  <div class="sol" style="left:154px;top:127px;"><svg viewBox="0 0 24 24"><rect x="3" y="3" width="18" height="18"/><circle cx="9" cy="9" r="2"/><path d="M3 18l6-6 4 4 3-3 5 5"/></svg><h4>Portfolio</h4><p>Tools that allow people companies to create content</p></div>
  <div class="sol" style="left:235px;top:127px;"><svg viewBox="0 0 24 24"><path d="M3 6h18M3 12h18M3 18h18"/><circle cx="8" cy="6" r="2"/><circle cx="15" cy="12" r="2"/><circle cx="10" cy="18" r="2"/></svg><h4>Evolution</h4><p>Tools that allow people companies to create content</p></div>
  <div class="sol" style="left:317px;top:127px;"><svg viewBox="0 0 24 24"><path d="M6 4h12l4 5-10 12L2 9l4-5zM2 9h20M12 21 8 9l4-5 4 5-4 12"/></svg><h4>Exclusive</h4><p>Tools that allow people companies to create content</p></div>
  <div class="footer"><b>Business</b> Presentation</div>
</section>

</body>
</html>
```